Corporate Business Card

Very professional, Modern, Not to busy, include phone address email, website
(253) 555-0174, 61807 19th Street N, Kent, WA 98517, marcus@kestrelbayholding.com, brelvanindustries.com

Target Market(s)

Manufacturing

Industry/Entity Type

Aero, machining, manufacturing, Off road racing

Contact Information for Business Card

Phone, address email, website

```html
<!DOCTYPE html>
<html lang="en">
<head>
<meta charset="utf-8">
<title>Brelvan Industries — Business Card</title>
<link rel="stylesheet" href="https://fonts.googleapis.com/css2?family=Montserrat:wght@400;500;700&display=swap">
<style>
  :root {
    --stage: #d9d9d9;
    --card-white: #ffffff;
    --brand-red: #d1232b;
    --brand-navy: #1b3370;
    --ink: #1c1c1c;
    --silver: #d4d4d4;
    --silver-soft: rgba(255, 255, 255, 0.10);
  }
  * { box-sizing: border-box; margin: 0; padding: 0; }
  html, body {
    width: 1200px;
    height: 856px;
    overflow: hidden;
    background: var(--stage);
    font-family: "Montserrat", Arial, sans-serif;
  }
  .canvas {
    position: relative;
    width: 1200px;
    height: 856px;
  }
  .card {
    position: absolute;
    top: 278px;
    width: 525px;
    height: 300px;
    overflow: hidden;
    box-shadow: 0 14px 30px rgba(0, 0, 0, 0.28);
  }
  .card--front { left: 40px; background: var(--card-white); }
  .card--back { left: 635px; background: var(--brand-red); }

  .card__wave {
    position: absolute;
    inset: 0;
    width: 100%;
    height: 100%;
  }

  /* Front */
  .brand {
    position: absolute;
    top: 38px;
    right: 28px;
    display: flex;
    align-items: center;
    gap: 8px;
  }
  .brand__mark {
    width: 12px;
    height: 12px;
    background: var(--brand-red);
  }
  .brand__name {
    font-weight: 700;
    font-size: 22px;
    letter-spacing: 0.5px;
    color: var(--brand-navy);
  }
  .brand__rule {
    position: absolute;
    top: 80px;
    left: 222px;
    width: 160px;
    height: 1.5px;
    background: var(--brand-navy);
  }
  .address {
    position: absolute;
    top: 124px;
    left: 30px;
    font-size: 12.5px;
    font-weight: 500;
    line-height: 1.35;
    color: var(--ink);
  }
  .contact {
    position: absolute;
    top: 178px;
    left: 60px;
    list-style: none;
  }
  .contact__item {
    display: flex;
    align-items: center;
    gap: 7px;
    font-size: 12px;
    font-weight: 500;
    line-height: 19px;
    color: var(--ink);
  }
  .contact__icon { width: 12px; height: 12px; flex: none; }

  /* Back */
  .card__map {
    position: absolute;
    top: 38px;
    left: 95px;
    width: 400px;
    height: 215px;
    border-radius: 40% 45% 35% 40%;
    background: radial-gradient(ellipse at center, var(--silver-soft), rgba(255,255,255,0) 70%);
  }
  .back-brand {
    position: absolute;
    top: 118px;
    left: 0;
    width: 100%;
    text-align: center;
    font-weight: 700;
    font-size: 38px;
    letter-spacing: 1px;
    color: var(--silver);
  }
  .back-rule {
    position: absolute;
    top: 182px;
    left: 60px;
    width: 200px;
    height: 2px;
    background: var(--silver);
  }
</style>
</head>
<body>
<main class="canvas">

  <section class="card card--front" aria-label="Business card front">
    <svg class="card__wave" viewBox="0 0 525 300" preserveAspectRatio="none" aria-hidden="true">
      <path d="M0 280 C260 280 360 260 420 180 C460 125 495 100 525 96 L525 300 L0 300 Z" fill="var(--brand-red)"/>
      <path d="M170 274 C300 268 368 248 414 184 C452 130 486 104 518 99" fill="none" stroke="var(--brand-navy)" stroke-width="3"/>
    </svg>

    <div class="brand">
      <span class="brand__mark"></span>
      <span class="brand__name">Brelvan Industries</span>
    </div>
    <div class="brand__rule"></div>

    <p class="address">61807 19th Street N<br>Kent, WA 98517</p>

    <ul class="contact">
      <li class="contact__item">
        <svg class="contact__icon" viewBox="0 0 12 12" aria-hidden="true"><path d="M2.5 1 L4.5 1 L5.2 3.5 L4 4.4 C4.6 5.8 6 7.3 7.6 8 L8.5 6.8 L11 7.5 L11 9.5 C11 10.4 10.3 11 9.4 11 C5 10.6 1.4 7 1 2.6 C1 1.7 1.6 1 2.5 1 Z" fill="var(--brand-red)"/></svg>
        (253) 555-0174
      </li>
      <li class="contact__item">
        <svg class="contact__icon" viewBox="0 0 12 12" aria-hidden="true"><rect x="0.5" y="2.5" width="11" height="7.5" fill="var(--brand-red)"/><path d="M0.8 2.8 L6 7 L11.2 2.8" fill="none" stroke="#fff" stroke-width="1"/></svg>
        marcus@kestrelbayholding.com
      </li>
      <li class="contact__item">
        <svg class="contact__icon" viewBox="0 0 12 12" aria-hidden="true"><circle cx="6" cy="6" r="5.5" fill="var(--brand-red)"/><path d="M0.5 6 H11.5 M6 0.5 C3.5 3 3.5 9 6 11.5 M6 0.5 C8.5 3 8.5 9 6 11.5" fill="none" stroke="#fff" stroke-width="0.8"/></svg>
        www.brelvanindustries.com
      </li>
    </ul>
  </section>

  <section class="card card--back" aria-label="Business card back">
    <div class="card__map" role="img" aria-label="Faint dotted world map in the background"></div>
    <p class="back-brand">Brelvan Industries</p>
    <div class="back-rule"></div>
  </section>

</main>
</body>
</html>
```